Software Product Flyer Design

A established czech software company needs a marketing flyer to promote their software product and its modules.
The overall feel of the flyer must to be serious, but also eye-catching, enticing, clever and bold to attract customers.
Unifying graphic element is the new product logo.
The flyer would be A4, colour both sides and folded once (to give 4 pages of A5).
Title page - product logo with module name and module icon, short presentation of the product and list of its key features.
Inside pages - detailed informations with screenshots or graphical schemas.
Back side - informations about technical requirements and user support, contacts (address, phone, fax, e-mail, web pages - no social networks).
Product logo, module icon and some images attached.
Updates
Hello,
Reason: For organizational reasons we extending the deadline by 10 days.
FYI: We have uploaded the new ZIP file with previous version of our flyer.
Attached PDF file with text for inner pages.
Target Market(s)
Existing or new customers like municipalities, public authorities and nonprofit organizations.
Industry/Entity Type
Marketing
Requirements
Must have
- Winning designer must provide a template for Adobe InDesign based on his graphic design.
Avoid to using exotic fonts - in Czech we use Latin Extended characters (like áéěíýůčřžšťďň).
Nice to have
- Using graphic motif from product logo like as attached splash screen.

```html
<!DOCTYPE html>
<html lang="en">
<head>
<meta charset="utf-8">
<title>Vero – product flyer</title>
<link rel="stylesheet" href="https://fonts.googleapis.com/css2?family=Roboto+Condensed:wght@300;400;700&display=swap">
<style>
:root{
  --orange:#e5541b;
  --dark:#45494c;
  --grey:#9a9a9a;
  --pale:#fbe0d3;
  --faint:#ececec;
  --rule:#3a3a3a;
  --paper:#ffffff;
  --shot:#e7ecef;
  --shot-edge:#b9c3c9;
}
*{box-sizing:border-box;margin:0;padding:0}
html,body{width:846px;height:1200px;overflow:hidden;background:var(--paper)}
body{font-family:"Roboto Condensed",Arial,sans-serif;color:var(--dark)}
.sheet{position:relative;width:846px;height:1200px;overflow:hidden}
.abs{position:absolute}

/* fold and page rules */
.rule-v{left:420px;top:0;width:1px;height:1200px;background:var(--rule)}
.rule-h{left:0;top:602px;width:846px;height:1px;background:var(--rule)}

/* wordmark */
.brand{display:flex;align-items:center;gap:10px;font-weight:700;color:var(--dark);letter-spacing:-1px;line-height:1}
.brand-mark{background:var(--orange);flex:none}
.brand--back{left:33px;top:244px;font-size:74px}
.brand--back .brand-mark{width:22px;height:22px}
.brand--cover{left:458px;top:240px;font-size:96px}
.brand--cover .brand-mark{width:30px;height:30px}
.brand--inside{left:33px;top:642px;font-size:60px}
.brand--inside .brand-mark{width:18px;height:18px}

/* faint vertical brand name */
.ghost-name{font-weight:700;color:var(--faint);font-size:118px;line-height:1;transform-origin:left top;transform:rotate(90deg);white-space:nowrap;letter-spacing:-2px}
.ghost-name--cover{left:846px;top:4px}
.ghost-name--inside{left:846px;top:612px}
.ghost-block{background:var(--pale);border-radius:14px}

/* back page */
.contact-box{left:212px;top:243px;width:209px;height:95px;background:var(--dark);color:#fff;padding:2px 6px;font-size:13.4px;line-height:17px;font-weight:300}
.contact-alt{left:218px;top:364px;width:190px;color:var(--grey);font-size:13.4px;line-height:17px;font-weight:300}

/* cover */
.cover-intro{left:550px;top:332px;width:260px;font-size:12.4px;line-height:17px}
.module-icon{left:690px;top:388px;width:88px;height:80px;border-radius:8px;background:linear-gradient(135deg,#dfe5ea,#9fb0bd)}
.cover-square{left:793px;top:552px;width:33px;height:33px;background:var(--orange)}

/* inside left */
.lead-small{left:229px;top:649px;width:142px;font-size:8.2px;line-height:11px;font-weight:700}
.frame-line{background:var(--orange)}
.band{left:0;top:695px;width:420px;height:255px;background:var(--orange)}
.band-col{top:709px;width:182px;color:#fff;font-size:11.6px;line-height:15.2px;font-weight:300}
.band-col p+p{margin-top:15px}
.band-col--a{left:36px}
.band-col--b{left:218px}
.screen{background:var(--shot);border:1px solid var(--shot-edge);box-shadow:0 1px 3px rgba(0,0,0,.25)}
.screen--small{left:218px;top:909px;width:172px;height:132px}
.screen--large{left:36px;top:976px;width:262px;height:188px}
.module-icon--inside{left:188px;top:985px;width:66px;height:74px}
.side-note{left:301px;top:1036px;width:86px;font-size:9px;line-height:11.5px}

/* inside right */
.step{left:455px;width:173px;height:120px}
.step--1{top:640px}.step--2{top:778px}.step--3{top:917px}
.step-no{left:455px;width:20px;height:19px;border-radius:4px;background:#b5b5b5;color:#fff;font-size:12px;line-height:19px;text-align:center;font-weight:300}
.step-text{left:640px;top:635px;width:180px;font-size:11.6px;line-height:15.2px;font-weight:300}
.step-text p+p{margin-top:15px}
.note-orange{left:640px;top:919px;width:206px;height:115px;background:var(--orange);color:#fff;padding:10px 12px;font-size:11.6px;line-height:15.2px;font-weight:300}
.note-dark{left:455px;top:1044px;width:237px;height:156px;background:var(--dark);color:#fff;padding:6px 4px;font-size:11.3px;line-height:15.2px;font-weight:300}
.pencil{left:726px;top:1028px;width:60px;height:64px;border-radius:6px;background:linear-gradient(135deg,#f6c23a,#e0892b)}
</style>
</head>
<body>
<main class="sheet">

  <!-- back page -->
  <section class="page page--back">
    <div class="abs brand brand--back"><span class="brand-mark"></span>Vero</div>
    <div class="abs contact-box">information on the technical and user support, contacts (address, phone, fax, email, web pages - without social networking).</div>
    <div class="abs contact-alt">information on the technical and user support, contacts (address, phone, fax, email, web pages - without social networking).</div>
  </section>

  <!-- cover -->
  <section class="page page--cover">
    <div class="abs ghost-name ghost-name--cover">Vero</div>
    <div class="abs ghost-block" style="left:800px;top:270px;width:46px;height:90px"></div>
    <div class="abs brand brand--cover"><span class="brand-mark"></span>Vero</div>
    <p class="abs cover-intro">Product brief introduction and a list of its main features, product brief introduction and a list of its main features</p>
    <div class="abs module-icon" role="img" aria-label="Module icon: notebook with a letter"></div>
    <div class="abs cover-square"></div>
  </section>

  <!-- inside left -->
  <section class="page page--inside-left">
    <div class="abs brand brand--inside"><span class="brand-mark"></span>Vero</div>
    <p class="abs lead-small">Detailed information graphics pictures or diagrams. detailed information graphics pictures or diagrams. detailed information</p>
    <div class="abs frame-line" style="left:370px;top:622px;width:265px;height:1px"></div>
    <div class="abs frame-line" style="left:370px;top:622px;width:1px;height:73px"></div>
    <div class="abs band"></div>
    <div class="abs band-col band-col--a">
      <p>Detailed information graphics pictures or diagrams. detailed information graphics pictures or diagrams. detailed information graphics pictures or diagrams.</p>
      <p>Detailed information graphics pictures or diagrams. detailed information graphics pictures or diagrams. detailed information graphics pictures or diagrams. detailed information graphics pictures or diagrams. detailed information graphics pictures or diagrams. detailed information graphics pictures</p>
    </div>
    <div class="abs band-col band-col--b">
      <p>or diagrams. detailed information graphics pictures or diagrams. detailed information graphics pictures or diagrams. detailed information graphics pictures or diagrams. detailed information graphics pictures or diagrams. detailed information graphics pictures or diagrams. detailed information graphics pictures or diagrams. detailed information graphics pictures or diagrams. detailed information graphics pictures or diagrams.</p>
    </div>
    <div class="abs ghost-block" style="left:0;top:960px;width:105px;height:190px;border-radius:0 30px 30px 0"></div>
    <div class="abs screen screen--small" role="img" aria-label="Application screenshot with data table"></div>
    <div class="abs screen screen--large" role="img" aria-label="Application screenshot with navigation tree and data table"></div>
    <div class="abs module-icon module-icon--inside" role="img" aria-label="Module icon: notebook with a letter"></div>
    <p class="abs side-note">Detailed information graphics pictures or diagrams. detailed information graphics pictures or diagrams. detailed information graphics pictures or diagrams. detailed information graphics pictures or diagrams. detailed information graphics pictures or diagrams. detailed</p>
  </section>

  <!-- inside right -->
  <section class="page page--inside-right">
    <div class="abs ghost-name ghost-name--inside">Vero</div>
    <div class="abs ghost-block" style="left:726px;top:1058px;width:104px;height:142px;background:var(--faint)"></div>
    <div class="abs frame-line" style="left:635px;top:622px;width:1px;height:283px"></div>
    <div class="abs frame-line" style="left:635px;top:904px;width:186px;height:1px"></div>

    <div class="abs screen step step--1" role="img" aria-label="Screenshot step 1: data table view"></div>
    <div class="abs step-no" style="top:742px">1</div>
    <div class="abs screen step step--2" role="img" aria-label="Screenshot step 2: data table view"></div>
    <div class="abs step-no" style="top:880px">2</div>
    <div class="abs screen step step--3" role="img" aria-label="Screenshot step 3: data table view"></div>
    <div class="abs step-no" style="top:1018px">3</div>

    <div class="abs step-text">
      <p>Detailed information graphics pictures or diagrams. detailed information graphics pictures or diagrams. detailed information graphics pictures or diagrams. detailed information graphics pictures or diagrams.</p>
      <p>Detailed information graphics pictures or diagrams. detailed information graphics pictures or diagrams. detailed information graphics pictures or diagrams. detailed information graphics pictures or diagrams. detailed information graphics pictures or diagrams.</p>
      <p>Detailed information graphics</p>
    </div>
    <div class="abs note-orange">Detailed information graphics pictures or diagrams. detailed information graphics pictures or diagrams. detailed information graphics pictures or diagrams. detailed information graphics</div>
    <div class="abs note-dark">Detailed information graphics pictures or diagrams. detailed information graphics pictures or diagrams. detailed information graphics pictures or diagrams. detailed information graphics pictures or diagrams. detailed information graphics pictures or diagrams. detailed information graphics pictures or diagrams. detailed information graphics pictures or diagrams.</div>
    <div class="abs pencil" role="img" aria-label="Pencil illustration"></div>
  </section>

  <div class="abs rule-v"></div>
  <div class="abs rule-h"></div>
</main>
</body>
</html>
```